SPIRIT ALBA/COPPERKNOLL DISTILLERY

DOUBLE SIDED BUSINESS CARD ONE SIDE FOR WWW.SPIRITALBA-EXAMPLE.ORG AND ONE SIDE FOR COPPERKNOLL DISTILLERY ARTWORK FOR WEBSITE IS ATTACHED

1)
GORDON PRICE CEO
SPIRIT ALBA
Office 4 Meridian Court
17 Larch Terrace
Glasgow
Scotland, G5 2QX
W:WWW.SPIRITALBA-EXAMPLE.ORG
E:GORDON@SPIRITALBA-EXAMPLE.ORG
T:+44 7412 559031

2)
GORDON PRICE CEO
COPPERKNOLL DISTILLERY
Building 148, Havenpark Rozendaal,
3e Berkenlaan, Katwijk, 2231KT

W: WWW.copperknolldistillery-example.nl
E: GORDON@copperknolldistillery-example.nl
T:+44 7412 559031

1)
Petra Vosberg DIRECTOR
SPIRIT ALBA
Office 4 Meridian Court
17 Larch Terrace
Glasgow
Scotland, G5 2QX
W:WWW.SPIRITALBA-EXAMPLE.ORG
E:Petra@SPIRITALBA-EXAMPLE.ORG
T:+31 6 58173420

2)
PETRA VOSBERG DIRECTOR
COPPERKNOLL DISTILLERY

E: petra@copperknolldistillery-example.nl
T:+31 6 58173420

```html
<!DOCTYPE html>
<html lang="en">
<head>
<meta charset="utf-8">
<title>Spirit Alba / Copperknoll Distillery – Business Cards</title>
<link rel="stylesheet" href="https://fonts.googleapis.com/css2?family=Montserrat:wght@400;500;700;800&display=swap">
<style>
  :root{
    --page:#161617;
    --card:#2e2e30;
    --card-dark:#262628;
    --gold:#c9a035;
    --gold-light:#e2b453;
    --ink:#232325;
    --white:#f4f4f4;
  }
  *{margin:0;padding:0;box-sizing:border-box}
  html,body{width:1200px;height:886px;overflow:hidden}
  body{background:var(--page);font-family:"Montserrat",Arial,sans-serif;position:relative}
  .card{
    position:absolute;left:240px;width:720px;height:400px;
    background:linear-gradient(135deg,var(--card) 0%,var(--card-dark) 100%);
    box-shadow:0 10px 30px rgba(0,0,0,.5);overflow:hidden;
  }
  .card--alba{top:30px}
  .card--copperknoll{top:456px}
  .card__name{
    position:absolute;left:52px;top:78px;color:var(--white);
    font-weight:800;font-size:30px;letter-spacing:3px;
  }
  .card__role{
    position:absolute;left:54px;top:116px;color:var(--gold);
    font-weight:500;font-size:14px;letter-spacing:1px;
  }
  .contact-band{
    position:absolute;left:0;top:168px;width:420px;height:96px;
    background:linear-gradient(90deg,var(--gold) 0%,var(--gold-light) 100%);
  }
  .card--copperknoll .contact-band{background:linear-gradient(90deg,var(--gold-light) 0%,#e8b655 100%)}
  .contact-band__icons{position:absolute;left:28px;top:40px;display:flex;flex-direction:column;gap:10px}
  .contact-band__icons svg{width:16px;height:16px;display:block}
  .contact-band__lines{position:absolute;left:70px;top:24px;color:var(--ink);font-size:13px;line-height:22px;letter-spacing:.8px}
  .contact-band__lines .email{font-size:11.5px;letter-spacing:1.2px}
  .address{
    position:absolute;left:52px;top:286px;color:var(--gold);
    font-size:14px;line-height:19px;font-weight:500;
  }
  .website{position:absolute;left:52px;color:var(--white);font-size:14px;font-weight:500;letter-spacing:.5px}
  .card--alba .website{top:364px}
  .card--copperknoll .website{top:340px}
  .accent-square{position:absolute;right:0;top:56px;width:74px;height:74px;background:var(--gold)}
  .card--copperknoll .accent-square{background:var(--gold-light)}
  .brand-name{
    position:absolute;left:430px;width:280px;top:180px;text-align:center;
    color:var(--gold);font-weight:700;font-size:30px;letter-spacing:5px;line-height:40px;
  }
  .card--copperknoll .brand-name{color:var(--gold-light);font-size:24px;letter-spacing:6px}
</style>
</head>
<body>

<section class="card card--alba" aria-label="Spirit Alba business card">
  <div class="accent-square"></div>
  <h1 class="card__name">GORDON PRICE</h1>
  <p class="card__role">CEO,SPIRIT ALBA</p>
  <div class="contact-band">
    <div class="contact-band__icons">
      <svg viewBox="0 0 16 16" aria-hidden="true"><path fill="#232325" d="M3.5 1.5l2.3 3-1.3 1.6c.8 1.9 2.3 3.4 4.2 4.2l1.6-1.3 3 2.3-1.2 2.4C7.4 13.5 2.5 8.6 1.3 2.7z"/></svg>
      <svg viewBox="0 0 16 16" aria-hidden="true"><rect x="1" y="3" width="14" height="10" fill="#232325"/><path d="M1.5 3.5L8 9l6.5-5.5" stroke="#d9ab45" stroke-width="1.3" fill="none"/></svg>
    </div>
    <div class="contact-band__lines">
      <div>+44 7412 559031</div>
      <div class="email">GORDON@SPIRITALBA-EXAMPLE.ORG</div>
    </div>
  </div>
  <p class="address">Office 4 Meridian Court<br>17 Larch Terrace<br>Glasgow<br>Scotland, G5 2QX</p>
  <p class="website">www.spiritalba-example.org/</p>
  <p class="brand-name">SPIRIT ALBA</p>
</section>

<section class="card card--copperknoll" aria-label="Copperknoll Distillery business card">
  <div class="accent-square"></div>
  <h2 class="card__name">GORDON PRICE</h2>
  <p class="card__role">CEO,COPPERKNOLL DISTILLERY</p>
  <div class="contact-band">
    <div class="contact-band__icons">
      <svg viewBox="0 0 16 16" aria-hidden="true"><path fill="#232325" d="M3.5 1.5l2.3 3-1.3 1.6c.8 1.9 2.3 3.4 4.2 4.2l1.6-1.3 3 2.3-1.2 2.4C7.4 13.5 2.5 8.6 1.3 2.7z"/></svg>
      <svg viewBox="0 0 16 16" aria-hidden="true"><rect x="1" y="3" width="14" height="10" fill="#232325"/><path d="M1.5 3.5L8 9l6.5-5.5" stroke="#e4b350" stroke-width="1.3" fill="none"/></svg>
    </div>
    <div class="contact-band__lines">
      <div>+44 7412 559031</div>
      <div class="email">GORDON@copperknolldistillery-example.nl</div>
    </div>
  </div>
  <p class="address">Building 148, Havenpark Rozendaal,<br>3e Berkenlaan, Katwijk, 2231KT</p>
  <p class="website">www.copperknolldistillery-example.nl</p>
  <p class="brand-name">COPPERKNOLL DISTILLERY</p>
</section>

</body>
</html>
```